Cover for Where the Quiet River Bends Beyond Our Morning

Cover for a book that describes everything that happens to a person, from pre-birth life plans through growing in compassion and wisdom to death and living in the afterlife. The information is revealed in messages from people living in the life after this life. The title is Lanterns Along the Hidden Stair of Every Soul: Gathered from Voices Dwelling in the Further Meadow. Author is T. Morven Ashdale. Book size is 6 by 9.

Target Market(s)

General

Font styles to use
Serif

```html
<!DOCTYPE html>
<html lang="en">
<head>
<meta charset="utf-8">
<title>Lanterns Along the Hidden Stair of Every Soul — T. Morven Ashdale</title>
<link rel="stylesheet" href="https://fonts.googleapis.com/css2?family=Allura&family=Source+Code+Pro:wght@700&display=swap">
<style>
  :root {
    --sky-blue: #29a8e0;
    --plum: #6a3290;
    --paper: #ffffff;
  }
  html, body {
    margin: 0;
    padding: 0;
    width: 804px;
    height: 1200px;
    overflow: hidden;
    background: var(--paper);
  }
  .cover {
    position: relative;
    width: 804px;
    height: 1200px;
    overflow: hidden;
    background: var(--paper);
  }
  .cover-art {
    position: absolute;
    inset: 0;
    width: 804px;
    height: 1200px;
  }
  .title-block {
    position: absolute;
    left: 0;
    top: 0;
    width: 804px;
    margin: 0;
    font-family: "Allura", cursive;
    font-weight: 400;
  }
  .title-lead {
    position: absolute;
    left: 190px;
    top: 106px;
    font-size: 40px;
    color: var(--sky-blue);
    white-space: nowrap;
  }
  .title-main {
    position: absolute;
    left: 40px;
    top: 146px;
    font-size: 92px;
    color: var(--sky-blue);
    white-space: nowrap;
    letter-spacing: 1px;
  }
  .title-tail {
    position: absolute;
    left: 64px;
    top: 240px;
    font-size: 48px;
    color: var(--plum);
    white-space: nowrap;
  }
  .subtitle {
    position: absolute;
    left: 0;
    top: 826px;
    width: 804px;
    margin: 0;
    text-align: center;
    font-family: "Source Code Pro", monospace;
    font-weight: 700;
    font-size: 27px;
    line-height: 40px;
    color: var(--sky-blue);
  }
  .divider {
    position: absolute;
    left: 132px;
    top: 930px;
    width: 540px;
    height: 20px;
  }
  .author {
    position: absolute;
    left: 0;
    top: 966px;
    width: 804px;
    margin: 0;
    text-align: center;
    font-family: "Source Code Pro", monospace;
    font-weight: 700;
    font-size: 26px;
    color: var(--sky-blue);
  }
</style>
</head>
<body>
<main class="cover">
  <svg class="cover-art" viewBox="0 0 804 1200" role="img" aria-label="Soft glowing illustration of an open hand reaching upward through violet and blue light among drifting orbs">
    <defs>
      <radialGradient id="glow-violet" cx="0.5" cy="0.5" r="0.5">
        <stop offset="0" stop-color="#8a77bd" stop-opacity="0.85"/>
        <stop offset="0.55" stop-color="#b5a6d6" stop-opacity="0.5"/>
        <stop offset="1" stop-color="#ffffff" stop-opacity="0"/>
      </radialGradient>
      <radialGradient id="glow-blue" cx="0.5" cy="0.5" r="0.5">
        <stop offset="0" stop-color="#5f86c9" stop-opacity="0.85"/>
        <stop offset="0.6" stop-color="#a9c6ea" stop-opacity="0.45"/>
        <stop offset="1" stop-color="#ffffff" stop-opacity="0"/>
      </radialGradient>
      <radialGradient id="orb-warm" r="0.5">
        <stop offset="0" stop-color="#f3b36a" stop-opacity="0.8"/>
        <stop offset="1" stop-color="#f3b36a" stop-opacity="0"/>
      </radialGradient>
      <radialGradient id="orb-red" r="0.5">
        <stop offset="0" stop-color="#e9704d" stop-opacity="0.85"/>
        <stop offset="1" stop-color="#e9704d" stop-opacity="0"/>
      </radialGradient>
      <radialGradient id="orb-purple" r="0.5">
        <stop offset="0" stop-color="#a455b0" stop-opacity="0.9"/>
        <stop offset="1" stop-color="#a455b0" stop-opacity="0"/>
      </radialGradient>
    </defs>
    <ellipse cx="250" cy="680" rx="300" ry="520" fill="url(#glow-violet)" transform="rotate(40 250 680)"/>
    <ellipse cx="500" cy="560" rx="260" ry="260" fill="url(#glow-blue)"/>
    <circle cx="440" cy="66" r="40" fill="url(#orb-purple)"/>
    <circle cx="470" cy="240" r="60" fill="url(#orb-warm)"/>
    <circle cx="590" cy="430" r="55" fill="url(#orb-red)"/>
    <circle cx="410" cy="880" r="75" fill="url(#orb-warm)"/>
    <circle cx="212" cy="1052" r="55" fill="url(#orb-warm)"/>
  </svg>

  <h1 class="title-block">
    <span class="title-lead">Lanterns Along</span>
    <span class="title-main">the Hidden Stair</span>
    <span class="title-tail">of Every Soul</span>
  </h1>

  <p class="subtitle">Gathered from Voices<br>Dwelling in the Further Meadow</p>

  <svg class="divider" viewBox="0 0 540 20" aria-hidden="true">
    <line x1="40" y1="7" x2="500" y2="7" stroke="#29a8e0" stroke-width="1.2"/>
    <line x1="40" y1="11" x2="500" y2="11" stroke="#29a8e0" stroke-width="3"/>
    <circle cx="26" cy="9" r="5" fill="none" stroke="#29a8e0" stroke-width="1.5"/>
    <circle cx="514" cy="9" r="5" fill="none" stroke="#29a8e0" stroke-width="1.5"/>
  </svg>

  <p class="author">By T. Morven Ashdale</p>
</main>
</body>
</html>
```